Adlinks Landing Page - DESIGN ONLY! PSD File

BACKGROUND:
Our website www.trailkit.com.au (running on Storlane) has a range of outdoor equipment being sold online. One of the products we specialize in is generators.
We are after a content landing page designed for Bluefin Adlinks to link to. This page should be focused on converting customers to sales as most customers at this stage of buying are ready to buy. We would like this page to focus on a combination of a professional graphic design and some text. The way it is laid out is open to your own experience, we just want it to look professional and have the right info for customers to convert.
THE BRIEF:
The page will include the range of products in the generator category that can be found here:
http://www.trailkit.com.au/generators.html
This page should include all the products within this category and should fit into to the color scheme and look of the website.
Most focus on the product should be placed in this order of priority, with special focus on the first two:
1. 2kva RRP: $1099 down to $499
2. 3.5kva RRP: $1399 down to $780
3. 3.5kva electric start RRP: $1599 down to $890
4. 4.4kva RRP: $1899 down to $950 (not currently listed, images will be provided soon)
5. 5kva RRP: $1999 down to $1150
The page can include a variety of graphic design, text and hyperlinks (or image clickable links), so please take this into account when making the graphics design.
The page must be discount oriented and include prices of each product as well as its original RRP price (crossed out), possible 'sale' graphics, and 'buy now' buttons linking to the product.
An example area this should fit within is the the column the products are on this page:
Other notes:
Our prices are truly bargains and the lowest in the market, so don't be afraid to express that in the design; texts like "Massive Sale" , "Priced to Clear Out" , "Won't Last Long at this Price"
Product images can be grabbed off the products here:
Deliverable will be a PSD file of the finished design.
We need these contact numbers included somewhere on this page:
NSW/ACT: 02 8555 0142
VIC/TAS: 03 9555 0176
SA: 08 7555 0193
NT/WA: 08 85550127

```html
<!DOCTYPE html>
<html lang="en">
<head>
<meta charset="utf-8">
<title>TrailKit – Generator Special Offers</title>
<link href="https://fonts.googleapis.com/css2?family=Carlito:wght@400;700&family=Russo+One&display=swap" rel="stylesheet">
<style>
  :root{
    --earth-dark:#1a1109;
    --earth-mid:#5a4330;
    --earth-light:#8a6d52;
    --nav-bg:#0a0a0a;
    --nav-link:#f0a04e;
    --nav-active:#ffffff;
    --hero-bg:#121212;
    --sale-red:#e4121b;
    --panel-top:#cdb8a6;
    --panel-bottom:#b9a491;
    --heading-grey:#5b524b;
    --text-dark:#1c1713;
    --pill-rrp:#b5a392;
    --pill-price:#7d6d5f;
    --ribbon:#d4721a;
    --footer-text:#b9aa9a;
    --brand-grey:#4a4a4a;
    --white:#ffffff;
  }
  *{box-sizing:border-box;margin:0;padding:0}
  html,body{width:999px;height:1200px;overflow:hidden}
  body{
    position:relative;
    font-family:"Carlito",Calibri,sans-serif;
    color:var(--text-dark);
    background:var(--earth-dark);
  }
  .earth-backdrop{
    position:absolute;inset:0;
    background:
      radial-gradient(ellipse 60% 55% at 50% 35%, rgba(138,109,82,.9), rgba(90,67,48,.7) 55%, rgba(26,17,9,1) 100%),
      linear-gradient(var(--earth-mid),var(--earth-dark));
  }
  .brand{
    position:absolute;left:186px;top:46px;
    display:flex;align-items:center;gap:10px;
    font-size:30px;font-weight:700;color:var(--brand-grey);
  }
  .brand-mark{width:22px;height:22px;background:var(--brand-grey)}
  .main-nav{
    position:absolute;left:390px;top:52px;width:482px;height:34px;
    background:var(--nav-bg);border-radius:17px;
    font-size:17px;
  }
  .main-nav a{position:absolute;top:7px;color:var(--nav-link);text-decoration:none}
  .main-nav a.is-active{color:var(--nav-active)}
  .hero{
    position:absolute;left:140px;top:114px;width:732px;height:394px;
    background:radial-gradient(ellipse at 70% 70%,#3a3430,var(--hero-bg) 70%);
    border-radius:12px 12px 0 0;overflow:hidden;
  }
  .hero-photo{
    position:absolute;border-radius:40px 40px 14px 14px;
    background:linear-gradient(150deg,#f0332a,#b80d10 70%,#6d0507);
  }
  .hero-tag{
    position:absolute;width:110px;height:76px;
    background:rgba(90,90,90,.55);border:1px solid rgba(255,255,255,.25);
    text-align:center;color:var(--white);
  }
  .hero-tag .name{font-size:19px;margin-top:3px}
  .hero-tag .rrp{font-size:14px;text-decoration:line-through;color:#ddd}
  .hero-tag .price{display:inline-block;background:var(--sale-red);font-size:17px;padding:0 6px;margin-top:2px}
  .hero-headline{
    position:absolute;right:28px;top:58px;
    font-family:"Russo One",sans-serif;font-size:35px;font-weight:400;color:var(--white);letter-spacing:-.5px;
  }
  .hero-sub{position:absolute;right:32px;top:116px;font-size:33px;color:var(--sale-red)}
  .hero-copy{position:absolute;right:28px;top:178px;text-align:right;font-size:21px;line-height:29px;color:#e6e6e6}
  .hero-copy mark{background:var(--sale-red);color:var(--white);padding:0 2px}
  .ribbon{
    position:absolute;right:-56px;bottom:42px;width:250px;height:36px;
    background:var(--ribbon);transform:rotate(-45deg);
    color:var(--white);font-size:17px;text-align:center;line-height:36px;
  }
  .offers{
    position:absolute;left:140px;top:508px;width:732px;height:497px;
    background:linear-gradient(var(--panel-top),var(--panel-bottom));
    border-radius:0 0 12px 12px;
  }
  .offers-title{position:absolute;left:41px;top:28px;font-size:19px;font-weight:400;color:var(--heading-grey)}
  .product{position:absolute;top:76px;width:150px}
  .product-photo{width:120px;height:118px;margin-left:8px;border-radius:22px 22px 8px 8px}
  .photo-red{background:linear-gradient(150deg,#f0332a,#b80d10 75%,#5e0406)}
  .photo-dark{background:linear-gradient(90deg,#222 0,#333 55%,#d81d1d 56%,#9b0c0c)}
  .product-name{margin-top:34px;font-size:16px;font-weight:700}
  .product-spec{font-size:14.5px;line-height:18px;white-space:nowrap}
  .pricing{position:absolute;top:246px;left:0;width:132px}
  .pill{height:24px;border-radius:12px;text-align:center;font-size:17px;line-height:24px;color:var(--white)}
  .pill-rrp{background:var(--pill-rrp);text-decoration:line-through}
  .pill-price{background:var(--pill-price);margin-top:5px}
  .buy-btn{
    display:flex;align-items:center;gap:8px;margin-top:6px;height:25px;padding-left:12px;
    background:linear-gradient(#e2141a,#b50b10);border:2px solid var(--white);border-radius:13px;
    color:var(--white);font-size:16px;text-decoration:none;
  }
  .buy-btn .plus{width:8px;height:8px;border:1px solid var(--white)}
  .divider{position:absolute;left:32px;top:439px;width:664px;height:1px;background:#9a8878}
  .delivery{
    position:absolute;left:32px;top:459px;width:546px;height:26px;
    background:linear-gradient(90deg,var(--sale-red),#a10a0e);
    clip-path:polygon(0 0,100% 0,98% 100%,0 100%);
    border-radius:13px 0 0 13px;
    color:var(--white);font-size:15px;line-height:26px;padding-left:13px;
  }
  .truck{position:absolute;left:540px;top:462px}
  .site-footer{position:absolute;left:0;top:1016px;width:999px;color:var(--footer-text);font-size:18px}
  .pay-label{position:absolute;left:179px;top:0}
  .cards{position:absolute;left:185px;top:36px;display:flex;gap:10px;font-size:11px;font-weight:700}
  .card{background:var(--white);color:#1a2a6c;padding:1px 4px}
  .contact-label{position:absolute;left:493px;top:0}
  .phones{position:absolute;right:168px;top:33px;text-align:right;color:var(--white);font-size:17px;line-height:21.5px}
</style>
</head>
<body>
  <div class="earth-backdrop" role="img" aria-label="Dry cracked earth texture fading to dark edges"></div>

  <div class="brand"><span class="brand-mark"></span>TrailKit</div>

  <nav class="main-nav">
    <a href="#" style="left:29px">Home</a>
    <a href="#" style="left:96px">New Products</a>
    <a href="#" class="is-active" style="left:224px">Special Offers</a>
    <a href="#" style="left:359px">Contact Us</a>
  </nav>

  <section class="hero">
    <div class="hero-photo" role="img" aria-label="Red portable inverter generator, 2kVA" style="left:25px;top:50px;width:200px;height:250px"></div>
    <div class="hero-photo" role="img" aria-label="Red portable inverter generator, 3.5kVA" style="left:192px;top:50px;width:240px;height:250px"></div>
    <div class="hero-tag" style="left:25px;top:294px">
      <div class="name">Silent 2kva</div>
      <div class="rrp">$1,099.00</div>
      <div class="price">$499.00</div>
    </div>
    <div class="hero-tag" style="left:234px;top:294px">
      <div class="name">Silent 3.5kva</div>
      <div class="rrp">$1,399.00</div>
      <div class="price">$780.00</div>
    </div>
    <h1 class="hero-headline">MASSIVE SALE</h1>
    <p class="hero-sub">Priced to clear</p>
    <p class="hero-copy">on selected generator<br>get <mark>50% discount</mark> and more</p>
    <div class="ribbon">*Limited stock</div>
  </section>

  <section class="offers">
    <h2 class="offers-title">Special offers on generators</h2>

    <article class="product" style="left:32px">
      <div class="product-photo photo-red" role="img" aria-label="Silent 2kVA red inverter generator"></div>
      <h3 class="product-name">Silent 2kVA</h3>
      <p class="product-spec">Pure Sine Wave<br>Inverter Generator</p>
      <div class="pricing">
        <div class="pill pill-rrp">$1,099.00</div>
        <div class="pill pill-price">$499.00</div>
        <a class="buy-btn" href="#"><span class="plus"></span>BUY NOW</a>
      </div>
    </article>

    <article class="product" style="left:200px">
      <div class="product-photo photo-red" role="img" aria-label="Silent 3.5kVA red inverter generator"></div>
      <h3 class="product-name">Silent 3.5kVA</h3>
      <p class="product-spec">Pure Sine Wave<br>Inverter Generator</p>
      <div class="pricing">
        <div class="pill pill-rrp">$1,399.00</div>
        <div class="pill pill-price">$780.00</div>
        <a class="buy-btn" href="#"><span class="plus"></span>BUY NOW</a>
      </div>
    </article>

    <article class="product" style="left:381px">
      <div class="product-photo photo-red" role="img" aria-label="Silent 3.5kVA electric start generator with control panel"></div>
      <h3 class="product-name">Silent 3.5kVA</h3>
      <p class="product-spec">Pure Sine Wave<br>Inverter Generator<br>Electric Start + Remote</p>
      <div class="pricing">
        <div class="pill pill-rrp">$1,599.00</div>
        <div class="pill pill-price">$890.00</div>
        <a class="buy-btn" href="#"><span class="plus"></span>BUY NOW</a>
      </div>
    </article>

    <article class="product" style="left:565px">
      <div class="product-photo photo-dark" role="img" aria-label="Silent 5kVA black and red generator"></div>
      <h3 class="product-name">Silent 5kVA</h3>
      <p class="product-spec">Pure Sine Wave<br>Inverter Generator<br>Electric Start + Remote</p>
      <div class="pricing">
        <div class="pill pill-rrp">$1,999.00</div>
        <div class="pill pill-price">$1,150.00</div>
        <a class="buy-btn" href="#"><span class="plus"></span>BUY NOW</a>
      </div>
    </article>

    <div class="divider"></div>
    <p class="delivery">And for only <b>$15 more</b>, get generator delivered to you anywhere in Australia</p>
    <svg class="truck" width="58" height="30" viewBox="0 0 58 30" aria-hidden="true">
      <rect x="6" y="4" width="30" height="18" fill="#2a2420"/>
      <path d="M37 9h10l8 8v5H37z" fill="#2a2420"/>
      <circle cx="15" cy="24" r="4" fill="#2a2420" stroke="#b9a491" stroke-width="1.5"/>
      <circle cx="46" cy="24" r="4" fill="#2a2420" stroke="#b9a491" stroke-width="1.5"/>
      <rect x="0" y="25" width="6" height="2" fill="#2a2420"/>
    </svg>
  </section>

  <footer class="site-footer">
    <p class="pay-label">Payment online may be done with:</p>
    <div class="cards"><span class="card">Vaultica</span><span class="card">Paynora</span></div>
    <p class="contact-label">For Additional Indormation please contact us:</p>
    <p class="phones">NSW/ACT: 02 8555 0142<br>VIC/TAS: 03 9555 0176<br>SA: 08 7555 0193<br>NT/WA: 08 85550127</p>
  </footer>
</body>
</html>
```